Graniteway Surface Works, Inc. Business Card

New business, we do epoxy, polishing concrete, underlayment, fluid applied flooring, sound proofing, double sided, will need 3 sets of cards with 3 different names and phone numbers.
Company: Graniteway Surface Works, Inc.
Address and Phone: 6339 Charlotte Pike PMB 2183Nashville, TN 38514
(615) 418-3927
www.granitewaysurfaceworks.example

Target Market(s)

General Contractors, Contractors, Architects

Contact Information for Business Card

1st Card: Devon Halvorsen C. 708.214.5873 e. devon@granitewaysurfaceworks.example
Vice President
2nd Card: Morgan Prescoe C. 708.389.6145 e. morgan@granitewaysurfaceworks.example
President
3rd Card: Bo Vu C. 405.631.8207 e. bo@granitewaysurfaceworks.example
Managing Partner

Font styles to use
Serif
Sans Serif

Requirements
Must have
• Professional Clean Design, Implement colors from Logo or nicely contrasting
Nice to have
• N/A

```html
<!DOCTYPE html>
<html lang="en">
<head>
<meta charset="utf-8">
<title>Graniteway Surface Works, Inc. – Business Card</title>
<link href="https://fonts.googleapis.com/css2?family=Montserrat:wght@500;700&family=Roboto:wght@400;700&display=swap" rel="stylesheet">
<style>
  :root {
    --brand-blue: #1b67b4;
    --brand-green: #6aa84f;
    --ink: #1a1a1a;
    --text: #2b2b2b;
    --pale-blue: #dde6f1;
    --pale-green: #e6efe3;
    --paper: #ffffff;
    --stage: #e9ebee;
  }
  * { box-sizing: border-box; margin: 0; padding: 0; }
  html, body {
    width: 1200px; height: 948px; overflow: hidden;
    background: var(--stage);
  }
  .sheet {
    position: relative; width: 1200px; height: 948px;
  }
  .card {
    position: absolute; left: 250px; width: 700px; height: 400px;
    border-radius: 26px; overflow: hidden;
    box-shadow: 0 6px 18px rgba(0,0,0,.12);
  }
  .card--back { top: 54px; background: var(--brand-blue); }
  .card--front { top: 494px; background: var(--paper); }

  /* back side */
  .back-wordmark {
    position: absolute; inset: 0;
    display: flex; align-items: center; justify-content: center; gap: 16px;
  }
  .back-wordmark .mark-square {
    width: 34px; height: 34px; border: 0; background: #ffffff;
  }
  .back-wordmark .company-name {
    font-family: "Montserrat", sans-serif; font-weight: 700;
    font-size: 30px; color: #ffffff; letter-spacing: .5px;
  }

  /* front side */
  .front-art {
    position: absolute; right: 0; top: 0; width: 330px; height: 100%;
    background: linear-gradient(135deg, var(--pale-blue) 0%, var(--pale-green) 100%);
  }
  .front-brand {
    position: absolute; left: 44px; top: 52px;
    display: flex; align-items: center; gap: 12px;
  }
  .front-brand .mark-square { width: 26px; height: 26px; background: var(--brand-blue); }
  .front-brand .company-name {
    font-family: "Montserrat", sans-serif; font-weight: 700;
    font-size: 20px; color: var(--ink);
    max-width: 280px; line-height: 1.2;
  }
  .person {
    position: absolute; left: 44px; top: 150px;
    padding-left: 18px; border-left: 6px solid var(--brand-blue);
  }
  .person .name {
    font-family: "Roboto", sans-serif; font-weight: 700;
    font-size: 30px; color: var(--brand-blue); letter-spacing: .3px;
  }
  .person .title {
    font-family: "Roboto", sans-serif; font-size: 17px; color: var(--text);
    margin-top: 2px;
  }
  .contact {
    position: absolute; left: 68px; top: 238px;
    font-family: "Roboto", sans-serif; font-size: 15px; color: var(--text);
    line-height: 1.45;
  }
  .contact .address { margin-bottom: 8px; }
  .contact ul { list-style: none; }
  .contact li { display: flex; align-items: center; gap: 8px; }
  .contact svg { width: 13px; height: 13px; flex: none; }
</style>
</head>
<body>
<main class="sheet">

  <section class="card card--back" aria-label="Card back">
    <div class="back-wordmark">
      <span class="mark-square"></span>
      <span class="company-name">Graniteway Surface Works, Inc.</span>
    </div>
  </section>

  <section class="card card--front" aria-label="Card front">
    <div class="front-art" role="img" aria-label="Faint brand decoration in pale blue and green"></div>

    <div class="front-brand">
      <span class="mark-square"></span>
      <span class="company-name">Graniteway Surface Works, Inc.</span>
    </div>

    <div class="person">
      <p class="name">DEVON HALVORSEN</p>
      <p class="title">Vice President</p>
    </div>

    <div class="contact">
      <p class="address">4812 Wendover Ridge PMB 7416<br>Nashville, TN 38514</p>
      <ul>
        <li>
          <svg viewBox="0 0 16 16" aria-hidden="true"><path fill="#6aa84f" d="M3.6 1.5l2.3 2.6-1.3 1.8c.9 2 2.5 3.6 4.5 4.5l1.8-1.3 2.6 2.3-1.5 2.1C6.8 13.3 2.7 9.2 1.5 3z"/></svg>
          708.214.5873
        </li>
        <li>
          <svg viewBox="0 0 16 16" aria-hidden="true"><rect x="1" y="3" width="14" height="10" rx="1" fill="#6aa84f"/><path d="M1.5 3.5L8 9l6.5-5.5" fill="none" stroke="#fff" stroke-width="1.3"/></svg>
          devon@granitewaysurfaceworks.example
        </li>
        <li>
          <svg viewBox="0 0 16 16" aria-hidden="true"><circle cx="8" cy="8" r="6.5" fill="none" stroke="#6aa84f" stroke-width="1.6"/><path d="M1.5 8h13M8 1.5c-3 3.5-3 9.5 0 13M8 1.5c3 3.5 3 9.5 0 13" fill="none" stroke="#6aa84f" stroke-width="1.1"/></svg>
          www.granitewaysurfaceworks.example
        </li>
      </ul>
    </div>
  </section>

</main>
</body>
</html>
```